*YO!!! Designers Needed!!* Front Page Cover Needed for a $$Billion Dollar$$ Company

We are a manufacturer of aluminum electrolytic capacitors. We are looking to create a front page cover that will be used on our annual report. We are a publicly listed company and work with many Pinnacle 300 companies, so your work will be viewed by the BIG GUNS and EXECUTIVES around the WORLD! If selected, you may be selected for additional work.

The front page cover should be unique. If elegance, modern, bling, and creativity somehow got together and had a child, that's what the cover page would look like!

Inspired Examples attached. Check them out!

www.velmoro.com

Font styles to use
Sans Serif

Requirements
Must have
• 1. Must include the attached logo. Logo size, color, and placement are at your discretion.

2. Should include the text, '2020 Annual Report'

3. The design should incorporate the use of foil and/or be embossed. The foil can be part of the design or can be the full page. See various examples attached for reference.

4. Shall be in A4 size and vertical orientation.
Nice to have
• Feel free to add any icons or stock photos (for example capacitors or circuit boards) if needed.

Be creative here and don't be afraid to be bold! The end product will be printed and budget is not a limiting factor, so feel free to make it extravagant if needed.

Our slogan is "Think Ahead". This slogan can or cannot be part of the theme.

```html
<!DOCTYPE html>
<html lang="en">
<head>
<meta charset="utf-8">
<title>Velmoro 2020 Annual Report Cover</title>
<link rel="stylesheet" href="https://fonts.googleapis.com/css2?family=Montserrat:wght@500;600&display=swap">
<style>
  :root {
    --backdrop: #2b2b2d;
    --cover-top: #1d1d20;
    --cover-bottom: #060607;
    --gold: #d9a93a;
    --gold-light: #f6df86;
    --gold-deep: #9c6d18;
  }
  * { margin: 0; padding: 0; box-sizing: border-box; }
  html, body {
    width: 726px;
    height: 1200px;
    overflow: hidden;
    background: var(--backdrop);
  }
  .canvas {
    position: relative;
    width: 726px;
    height: 1200px;
  }
  .cover {
    position: absolute;
    left: 0;
    top: 86px;
    width: 726px;
    height: 1027px;
    background: linear-gradient(160deg, var(--cover-top) 0%, #101012 45%, var(--cover-bottom) 100%);
    overflow: hidden;
  }
  .foil-lines {
    position: absolute;
    inset: 0;
    width: 726px;
    height: 1027px;
  }
  .brand {
    position: absolute;
    left: 0;
    top: 92px;
    width: 726px;
    text-align: center;
    font-family: "Montserrat", sans-serif;
    font-weight: 600;
    font-size: 44px;
    letter-spacing: 1px;
    line-height: 1;
    color: var(--gold);
  }
  .slogan {
    position: absolute;
    right: 270px;
    top: 148px;
    font-family: "Montserrat", sans-serif;
    font-weight: 500;
    font-size: 10px;
    letter-spacing: 0.5px;
    color: var(--gold);
  }
  .report-title {
    position: absolute;
    left: 70px;
    top: 664px;
    font-family: "Montserrat", sans-serif;
    font-weight: 600;
    font-size: 98px;
    line-height: 88px;
    letter-spacing: -1px;
    background: linear-gradient(180deg, var(--gold-light) 0%, var(--gold) 45%, var(--gold-deep) 100%);
    -webkit-background-clip: text;
    background-clip: text;
    color: transparent;
  }
  .report-title span { display: block; }
</style>
</head>
<body>
<main class="canvas">
  <section class="cover">
    <svg class="foil-lines" viewBox="0 0 726 1027" aria-hidden="true">
      <defs>
        <linearGradient id="foil" x1="0" y1="0" x2="1" y2="1">
          <stop offset="0" stop-color="#f6df86"/>
          <stop offset="0.5" stop-color="#d9a93a"/>
          <stop offset="1" stop-color="#a8761c"/>
        </linearGradient>
      </defs>
      <rect class="frame" x="34" y="39" width="656" height="947" fill="none" stroke="url(#foil)" stroke-width="3"/>
      <line x1="476" y1="39" x2="690" y2="352" stroke="url(#foil)" stroke-width="2.5"/>
      <line x1="551" y1="39" x2="690" y2="640" stroke="url(#foil)" stroke-width="2.5"/>
      <line x1="690" y1="560" x2="512" y2="986" stroke="url(#foil)" stroke-width="2.5"/>
      <line x1="600" y1="228" x2="690" y2="470" stroke="url(#foil)" stroke-width="2"/>
    </svg>
    <div class="brand">Velmoro</div>
    <div class="slogan">BUILT TO LAST.</div>
    <h1 class="report-title">
      <span>2020</span>
      <span>ANNUAL</span>
      <span>REPORT</span>
    </h1>
  </section>
</main>
</body>
</html>
```